Stationery Design Project - KORVELT-NINE

Presentation Folder
Size: A4
Notepad
Size: 250mm x 140mm
With Compliments Slip
Size: DL
210mm x 99mm
Letterhead
Size: A4 - 210mm x 297mm
Business Cards
Size: 90mm x 55mm

Company is called "KORVELT-NINE"
website: www.korveltnine.com.au (under construction)

Offices: *Perth *Brisbane *Seoul *Hong Kong

If you need any further information please let me know!

Cheers

Lionel

```html
<!DOCTYPE html>
<html lang="en">
<head>
<meta charset="utf-8">
<title>KORVELT-NINE Presentation Folder</title>
<link href="https://fonts.googleapis.com/css2?family=Roboto:wght@300;400;500&family=Arimo:wght@400;700&display=swap" rel="stylesheet">
<style>
  :root {
    --backdrop: #4a4a4a;
    --paper: #ffffff;
    --band-blue: #1a5ea6;
    --accent-cyan: #1d9ac9;
    --ink: #1e1e1e;
    --muted: #9a9a9a;
    --fold: #d6d6d6;
  }
  html, body {
    margin: 0;
    padding: 0;
    width: 1200px;
    height: 904px;
    overflow: hidden;
    background: var(--backdrop);
  }
  .folder {
    position: absolute;
    left: 109px;
    top: 81px;
    width: 995px;
    height: 699px;
    background: var(--paper);
    box-shadow: 0 4px 14px rgba(0,0,0,.35);
  }
  .panel { position: absolute; top: 0; height: 699px; overflow: hidden; }
  .panel--back { left: 0; width: 495px; }
  .panel--front { left: 502px; width: 493px; }
  .fold-line {
    position: absolute; left: 495px; top: 0; width: 7px; height: 699px;
    border-left: 1px solid var(--fold); border-right: 1px solid var(--fold);
    box-sizing: border-box;
  }
  .base-band {
    position: absolute; left: 0; bottom: 0; width: 100%; height: 30px;
    background: var(--band-blue);
  }
  .wordmark {
    position: absolute;
    display: flex; align-items: center; gap: 8px;
    font-family: "Roboto", sans-serif; font-weight: 300;
    color: #5a5a5a; letter-spacing: .06em;
  }
  .wordmark__square { background: var(--accent-cyan); }
  .panel--back .wordmark { left: 0; width: 495px; justify-content: center; top: 66px; font-size: 15px; }
  .panel--back .wordmark__square { width: 14px; height: 14px; }
  .tagline {
    position: absolute; top: 132px; left: 0; width: 495px; margin: 0;
    text-align: center; font-family: "Roboto", sans-serif; font-weight: 400;
    font-size: 18.5px; line-height: 24px; color: var(--accent-cyan);
  }
  .cube-fade {
    position: absolute; left: 221px; top: 424px; width: 274px; height: 245px;
    background: linear-gradient(160deg, rgba(255,255,255,0) 5%, #ececec 45%, #dcdcdc 75%, #e8e8e8 100%);
    clip-path: polygon(30% 0, 100% 0, 100% 100%, 0 100%, 0 30%);
  }
  .offices {
    position: absolute; top: 553px; left: 31px;
    display: grid; grid-template-columns: 113px 112px 119px 112px;
    font-family: "Arimo", sans-serif; font-size: 8px; line-height: 11px; color: var(--ink);
  }
  .office__name {
    margin: 0 0 15px; font-weight: 400; font-size: 9px; color: var(--accent-cyan);
    letter-spacing: .02em;
  }
  .office__address { margin: 0 0 9px; }
  .office__contact { margin: 0; }
  .office__contact span { display: inline-block; width: 15px; }
  .panel--front .wordmark { left: 146px; top: 86px; font-size: 24px; color: #6b6b6b; gap: 12px; }
  .panel--front .wordmark__square { width: 40px; height: 40px; }
  .office-cities {
    position: absolute; left: 237px; top: 123px; margin: 0; padding: 0; list-style: none;
    font-family: "Roboto", sans-serif; font-size: 10.5px; line-height: 14px; color: var(--muted);
  }
  .cube-hero {
    position: absolute; left: 139px; top: 264px; width: 354px; height: 318px;
    background: linear-gradient(150deg, #ffffff 0%, #e9f2fa 30%, #bcd9f1 60%, #e6eef6 85%, #ffffff 100%);
    clip-path: polygon(20% 0, 100% 0, 100% 100%, 8% 100%, 0 20%);
  }
  .photo-strip {
    position: absolute; left: 0; top: 581px; width: 493px; height: 88px;
    display: grid; grid-template-columns: repeat(4, 1fr);
  }
  .photo--stacker { background: linear-gradient(180deg, #6f95c4 0%, #8a7658 60%, #8c4b2a 100%); }
  .photo--turbine { background: linear-gradient(180deg, #8eaecb 0%, #c9d6e2 50%, #5a7693 100%); }
  .photo--platform { background: linear-gradient(180deg, #2d4e78 0%, #1c3a63 60%, #0e2445 100%); }
  .photo--carrier { background: linear-gradient(180deg, #4f6b87 0%, #2d4b6a 60%, #1a3550 100%); }
</style>
</head>
<body>
  <div class="folder">
    <section class="panel panel--back">
      <div class="wordmark"><span class="wordmark__square"></span>KORVELT-NINE</div>
      <p class="tagline">Australia's number one group<br>in health, safety, environmental<br>and quality recruitment.</p>
      <div class="cube-fade" role="img" aria-label="Faint grey three-dimensional block cube decoration"></div>
      <div class="offices">
        <div class="office">
          <h3 class="office__name">PERTH OFFICE</h3>
          <p class="office__address">Suite 4, 212 Harlow Street<br>Westmere<br>Western Australia 6010</p>
          <p class="office__contact"><span>P|</span>+61 (0) 8 6390 2718<br><span>F|</span>+61 (0) 8 6390 2719<br><span>E|</span>info@korveltnine.com.au</p>
        </div>
        <div class="office">
          <h3 class="office__name">BRISBANE OFFICE</h3>
          <p class="office__address">Level 18, Tallis House<br>120 Merrow Street, Brisbane<br>Queensland 4001</p>
          <p class="office__contact"><span>P|</span>+61 (0) 7 3140 5583<br><span>F|</span>+61 (0) 7 3140 5584<br><span>E|</span>info@korveltnine.com.au</p>
        </div>
        <div class="office">
          <h3 class="office__name">SEOUL OFFICE</h3>
          <p class="office__address">Level 27, Hanbit Tower<br>402 Seorin-ro<br>Daemyung dong, Junam-Gu<br>Seoul, Republic of Korea</p>
          <p class="office__contact" style="margin-top:-9px"><span>P|</span>+82 (0) 2 6104 3370<br><span>F|</span>+82 (0) 2 6104 3371<br><span>E|</span>mirena@korveltnine.com.au</p>
        </div>
        <div class="office">
          <h3 class="office__name">PERTH OFFICE</h3>
          <p class="office__address">Suite 4, 212 Harlow Street<br>Westmere<br>Western Australia 6010</p>
          <p class="office__contact"><span>P|</span>+61 (0) 8 6390 2718<br><span>F|</span>+61 (0) 8 6390 2719<br><span>E|</span>info@korveltnine.com.au</p>
        </div>
      </div>
      <div class="base-band"></div>
    </section>

    <div class="fold-line"></div>

    <section class="panel panel--front">
      <div class="wordmark"><span class="wordmark__square"></span>KORVELT-NINE</div>
      <ul class="office-cities">
        <li>Perth</li>
        <li>Brisbane</li>
        <li>Seoul</li>
        <li>Hong Kong</li>
      </ul>
      <div class="cube-hero" role="img" aria-label="Large white and translucent blue three-dimensional block cube illustration"></div>
      <div class="photo-strip">
        <div class="photo--stacker" role="img" aria-label="Photo of a mining stacker machine on red earth"></div>
        <div class="photo--turbine" role="img" aria-label="Photo of a wind turbine over the sea"></div>
        <div class="photo--platform" role="img" aria-label="Aerial photo of an offshore oil platform"></div>
        <div class="photo--carrier" role="img" aria-label="Aerial photo of a gas carrier ship at sea"></div>
      </div>
      <div class="base-band"></div>
    </section>
  </div>
</body>
</html>
```